Modern Spot UV Business Card design

We are a relatively new real estate agency. We need a business card that reflects the professionalism and prestige of our company but is also modern and fresh, based around our logo.
We would love to utilise spot UV.
Happy to let the designers use their imagination and see what they come up with (we're not very creative, so have no ideas for you, sorry) :-)
We'd like one for each staff member, but I've just provided one staff members photo here to avoid confusion.

Target Market(s)

Families

Industry/Entity Type

Real Estate Agent

Contact Information for Business Card

Dale Verco - Director & Principal
Mobile: 0491 627 540
Email: dale.verco@vbrokers.example.au
Phone: (08) 8374 6150
Fax: (08) 8374 6198
www.vercobrokersproperty.example.au

Font styles to use
Other font styles liked:
• Kabel Dm BT

Requirements
Must have
• Contact details, logo, photo, spot UV
Nice to have
• Modern interesting features that will make people comment. Nothing too feminine nor too masculine.
Should not have
• No houses! Nothing typical of a real estate agent.

```html
<!DOCTYPE html>
<html lang="en">
<head>
<meta charset="utf-8">
<title>Verco Brokers Property – Business Card</title>
<link rel="stylesheet" href="https://fonts.googleapis.com/css2?family=Lato:wght@400;700;900&display=swap">
<style>
  :root {
    --page: #e9e9e9;
    --uv-grey: #6e6e6e;
    --uv-gloss: #3c3c3c;
    --uv-line: #9a9a9a;
    --uv-text: #d8d8d8;
    --ink: #1f1f1f;
    --ink-soft: #3a3a3a;
    --brand-blue: #1a8fd0;
    --brand-orange: #f39324;
    --paper: #ffffff;
  }
  * { box-sizing: border-box; margin: 0; padding: 0; }
  html, body { width: 1200px; height: 810px; overflow: hidden; }
  body {
    background: var(--page);
    font-family: "Lato", sans-serif;
    display: flex;
    align-items: center;
    justify-content: center;
    gap: 30px;
  }
  .card {
    position: relative;
    width: 560px;
    height: 343px;
    overflow: hidden;
    box-shadow: 0 6px 18px rgba(0,0,0,.18);
  }

  /* Front: spot UV side */
  .card--front {
    background: var(--uv-grey);
    display: flex;
    flex-direction: column;
    align-items: center;
    justify-content: center;
  }
  .front-brand {
    display: flex;
    align-items: center;
    gap: 16px;
  }
  .brand-name--uv {
    font-weight: 900;
    font-size: 44px;
    line-height: 1;
    color: var(--uv-gloss);
    letter-spacing: -0.5px;
    white-space: nowrap;
  }
  .front-tagline {
    border-left: 1px solid var(--uv-line);
    padding-left: 12px;
    font-size: 16px;
    line-height: 1.15;
    color: var(--uv-gloss);
    letter-spacing: 1px;
    white-space: nowrap;
  }
  .front-web {
    margin-top: 40px;
    display: flex;
    align-items: center;
    gap: 10px;
    font-size: 12px;
    color: var(--uv-text);
    letter-spacing: .3px;
  }
  .front-web::before, .front-web::after {
    content: "";
    width: 70px;
    height: 1px;
    background: var(--uv-line);
  }

  /* Back: contact side */
  .card--back { background: var(--paper); }
  .portrait {
    position: absolute;
    right: 0;
    top: 0;
    width: 230px;
    height: 270px;
    background: linear-gradient(170deg, #f3f3f3 0%, #c9b4a6 35%, #5b6068 70%, #3f444b 100%);
  }
  .back-brand {
    position: absolute;
    left: 28px;
    top: 58px;
    display: flex;
    align-items: center;
    gap: 10px;
  }
  .brand-mark {
    width: 14px;
    height: 14px;
    border-radius: 50%;
    background: var(--brand-orange);
  }
  .brand-name {
    font-weight: 900;
    font-size: 28px;
    color: var(--ink);
    letter-spacing: -0.3px;
    line-height: 1;
    white-space: nowrap;
  }
  .back-tagline {
    border-left: 1px solid #999;
    padding-left: 8px;
    font-size: 10px;
    line-height: 1.15;
    color: var(--ink-soft);
    letter-spacing: .5px;
    white-space: nowrap;
  }
  .person {
    position: absolute;
    left: 28px;
    top: 130px;
  }
  .person-name {
    font-weight: 900;
    font-size: 24px;
    color: var(--brand-blue);
    line-height: 1;
  }
  .person-role {
    font-size: 13px;
    color: var(--ink);
    margin-top: 3px;
  }
  .contact-list {
    list-style: none;
    margin-top: 10px;
  }
  .contact-list li {
    display: flex;
    align-items: center;
    gap: 8px;
    font-size: 13px;
    color: var(--ink);
    line-height: 20px;
  }
  .contact-list svg { width: 13px; height: 13px; flex: none; }
  .contact-list .highlight { color: var(--brand-blue); }
  .swoosh {
    position: absolute;
    left: 0;
    bottom: 0;
    width: 560px;
    height: 120px;
  }
</style>
</head>
<body>

  <section class="card card--front" aria-label="Card front">
    <div class="front-brand">
      <span class="brand-name--uv">Verco Brokers</span>
      <span class="front-tagline">Guiding you towards<br>a new address</span>
    </div>
    <p class="front-web">www.vercobrokersproperty.example.au</p>
  </section>

  <section class="card card--back" aria-label="Card back">
    <div class="portrait" role="img" aria-label="Portrait photo of the agent in a grey suit"></div>

    <svg class="swoosh" viewBox="0 0 560 120" preserveAspectRatio="none">
      <path d="M0 95 C150 80 300 70 430 40 C480 28 530 15 560 0 L560 6 C520 30 470 45 420 55 C300 80 160 92 0 103 Z" fill="var(--brand-orange)"/>
      <path d="M0 103 C160 92 300 80 420 55 C470 45 520 30 560 10 L560 120 L0 120 Z" fill="var(--brand-blue)"/>
      <path d="M0 110 C200 100 360 90 560 60 L560 120 L0 120 Z" fill="#1480bd"/>
    </svg>

    <div class="back-brand">
      <span class="brand-mark"></span>
      <span class="brand-name">Verco Brokers</span>
      <span class="back-tagline">Guiding you towards<br>a new address</span>
    </div>

    <div class="person">
      <h1 class="person-name">Dale Verco</h1>
      <p class="person-role">Director &amp; Principal</p>
      <ul class="contact-list">
        <li>
          <svg viewBox="0 0 16 16"><path d="M3 1l3 3-2 2c1 2 3 4 5 5l2-2 3 3-2 3C7 15 1 9 1 3z" fill="var(--brand-blue)"/></svg>
          (08) 8374 6150
        </li>
        <li>
          <svg viewBox="0 0 16 16"><rect x="4" y="1" width="8" height="14" rx="1.5" fill="none" stroke="var(--brand-blue)" stroke-width="1.6"/><circle cx="8" cy="12.5" r="1" fill="var(--brand-blue)"/></svg>
          0491 627 540
        </li>
        <li>
          <svg viewBox="0 0 16 16"><rect x="4" y="1" width="8" height="5" fill="var(--brand-blue)"/><rect x="1" y="6" width="14" height="6" rx="1" fill="var(--brand-blue)"/><rect x="4" y="10" width="8" height="5" fill="#fff" stroke="var(--brand-blue)" stroke-width="1.2"/></svg>
          (08) 8374 6198
        </li>
        <li>
          <svg viewBox="0 0 16 16"><rect x="1" y="3" width="14" height="10" rx="1" fill="var(--brand-blue)"/><path d="M1 4l7 5 7-5" fill="none" stroke="#fff" stroke-width="1.2"/></svg>
          dale.verco@vbrokers.example.au
        </li>
        <li>
          <svg viewBox="0 0 16 16"><circle cx="8" cy="8" r="6.5" fill="none" stroke="var(--brand-blue)" stroke-width="1.4"/><ellipse cx="8" cy="8" rx="3" ry="6.5" fill="none" stroke="var(--brand-blue)" stroke-width="1.1"/><path d="M1.5 8h13M3 4.5h10M3 11.5h10" stroke="var(--brand-blue)" stroke-width="1"/></svg>
          <span>www.<span class="highlight">vercobrokersproperty</span>.example.au</span>
        </li>
      </ul>
    </div>
  </section>

</body>
</html>
```